Website Banner Ad Design - 4x 200x200px panels that will rotate

I'm looking for four (4) 200x200px "panels" that will rotate on a website. Each one should have a unique description or key words on it, that makes it attractive to customers. It is important that each individual one kinda fits to our logo design to give it a "uniform" design.
The first panel should just be our logo and a slogan that says "AFFORDABLE. ACCELERATED. EFFECTIVE." This panel should also list our website "www.vortanex.com"
The second panel should have the following key text:
- Accelerated Training Courses
- Private Pilot in 4-weeks
- Career Programs from PPL to CFII
- Pay-as-you-go
The third panel should have the following key text:
- Advanced Training
- Firefighting (KTRA) & Forestry Tactics Training
- ZX 340 & Orin 318K Turbine Transition Training
- External-Load (VR) Courses
THE fourth panel should list our website address "www.vortanex.com" and phone number: (555) 270-4381.
I give free hand with the design. Any idea is welcome. See attached some photos and logo that can be used. If you visit http://www.vanemarket.com/PROGRAMHUB/tabid/738/Default.aspx you can see other 200x200 panels to get an idea of what we're looking for. Our look has to be professional and stick out from the rest of our competitors. By questions, just PM me.

```html
<!DOCTYPE html>
<html lang="en">
<head>
<meta charset="utf-8">
<title>Vortanex Rotating Banner Panels</title>
<link rel="stylesheet" href="https://fonts.googleapis.com/css2?family=Source+Sans+3:wght@400;600;700;900&display=swap">
<style>
  :root {
    --canvas-bg: #d3d3d3;
    --text-light: #ffffff;
    --sky-blue: #3f6fa8;
    --deep-navy: #1d3559;
    --grass-green: #4f7a2c;
    --tarmac-grey: #6e7278;
    --room-beige: #8a8478;
    --shade: rgba(15, 28, 48, 0.28);
  }
  html, body {
    margin: 0;
    padding: 0;
    width: 1200px;
    height: 1200px;
    overflow: hidden;
    background: var(--canvas-bg);
    font-family: "Source Sans 3", "Source Sans Pro", Arial, sans-serif;
  }
  .canvas {
    position: relative;
    width: 1200px;
    height: 1200px;
  }
  .panel {
    position: absolute;
    overflow: hidden;
    color: var(--text-light);
  }
  .panel--slogan   { left: 50px;  top: 52px;  width: 441px; height: 441px; }
  .panel--courses  { left: 605px; top: 52px;  width: 441px; height: 441px; }
  .panel--advanced { left: 55px;  top: 619px; width: 454px; height: 439px; }
  .panel--contact  { left: 605px; top: 614px; width: 441px; height: 441px; }

  .photo {
    position: absolute;
    inset: 0;
  }
  .photo--helicopter-field {
    background: linear-gradient(180deg, #2f5d98 0%, #8eaed0 32%, #c9ced4 48%, var(--grass-green) 66%, var(--tarmac-grey) 80%, #3f6a22 100%);
  }
  .photo--pilots-tarmac {
    background: linear-gradient(180deg, #9fb6cc 0%, #5f8a44 30%, var(--deep-navy) 55%, #505b69 100%);
  }
  .photo--classroom {
    background: linear-gradient(135deg, #c3c2bd 0%, var(--room-beige) 40%, #3f4856 75%, var(--deep-navy) 100%);
  }
  .photo--cockpit-view {
    background: linear-gradient(120deg, #17304f 0%, var(--sky-blue) 40%, #b9c8d6 62%, #5e7f48 100%);
  }
  .shade {
    position: absolute;
    inset: 0;
    background: var(--shade);
  }

  .brand-name {
    position: absolute;
    left: 18px;
    top: 28px;
    margin: 0;
    font-size: 70px;
    font-weight: 900;
    line-height: 1;
    letter-spacing: -1px;
    color: var(--text-light);
  }

  .slogan {
    position: absolute;
    left: 38px;
    top: 182px;
    margin: 0;
    padding: 0;
    list-style: none;
    font-size: 42px;
    font-weight: 600;
    line-height: 56px;
    letter-spacing: 0.5px;
  }

  .web-address {
    position: absolute;
    margin: 0;
    font-weight: 400;
  }
  .panel--slogan .web-address {
    left: 46px;
    top: 380px;
    font-size: 33px;
  }
  .panel--contact .web-address {
    left: 20px;
    top: 392px;
    font-size: 27px;
    font-weight: 600;
  }

  .feature-list {
    position: absolute;
    margin: 0;
    padding: 0;
    list-style: none;
    font-weight: 600;
  }
  .feature-list li::before {
    content: "\2022";
    margin-right: 4px;
    font-size: 0.7em;
    vertical-align: 0.15em;
  }
  .panel--courses .feature-list {
    left: 11px;
    top: 198px;
    font-size: 26px;
    line-height: 46.5px;
  }
  .panel--advanced .feature-list {
    left: 15px;
    top: 211px;
    font-size: 22px;
    line-height: 46.5px;
    letter-spacing: -1px;
  }

  .phone-number {
    position: absolute;
    left: 18px;
    top: 284px;
    margin: 0;
    font-size: 53px;
    font-weight: 700;
    line-height: 1;
  }
</style>
</head>
<body>
<main class="canvas">

  <section class="panel panel--slogan">
    <div class="photo photo--helicopter-field" role="img" aria-label="Photo of a white training helicopter parked on grass under a cloudy blue sky"></div>
    <div class="shade"></div>
    <p class="brand-name">vortanex</p>
    <ul class="slogan">
      <li>AFFORDABLE</li>
      <li>ACCELERATED</li>
      <li>EFFECTIVE</li>
    </ul>
    <p class="web-address">www.vortanex.com</p>
  </section>

  <section class="panel panel--courses">
    <div class="photo photo--pilots-tarmac" role="img" aria-label="Photo of two pilots in navy flight suits standing beside a helicopter on the tarmac"></div>
    <div class="shade"></div>
    <p class="brand-name">vortanex</p>
    <ul class="feature-list">
      <li>Accelerated Training Courses</li>
      <li>Private Pilot in 4-weeks</li>
      <li>Career Programs from PPL to CFII</li>
      <li>Pay-as-you-go</li>
    </ul>
  </section>

  <section class="panel panel--advanced">
    <div class="photo photo--classroom" role="img" aria-label="Photo of an instructor teaching a ground school class in a meeting room"></div>
    <div class="shade"></div>
    <p class="brand-name">vortanex</p>
    <ul class="feature-list">
      <li>Advanced Training</li>
      <li>Firefighting (KTRA) &amp; Forestry Tactics Training</li>
      <li>ZX 340 &amp; Orin 318K Turbine Transition Training</li>
      <li>External-Load (VR) Courses</li>
    </ul>
  </section>

  <section class="panel panel--contact">
    <div class="photo photo--cockpit-view" role="img" aria-label="Photo of a helmeted pilot leaning out of a helicopter door above green countryside"></div>
    <div class="shade"></div>
    <p class="brand-name">vortanex</p>
    <p class="phone-number">(555) 270-4381</p>
    <p class="web-address">www.vortanex.com</p>
  </section>

</main>
</body>
</html>
```